Bref créative
Stationary and Business cards for Criminal Defense Firm
Daniel R. Halvorsen - Attorney at Law
Professional
Daniel R Halvorsen
418 N. 7th Street
Columbus, OH 43207
Daniel@verdictwithhalvorsen.example
VerdictWithHalvorsen.example

```html
<!DOCTYPE html>
<html lang="en">
<head>
<meta charset="utf-8">
<title>Daniel R. Halvorsen – Stationery Concepts</title>
<link href="https://fonts.googleapis.com/css2?family=Cinzel:wght@600&family=Lato:wght@400;700&display=swap" rel="stylesheet">
<style>
:root{
  --navy:#2b2773;
  --navy-dark:#1f1c58;
  --paper:#ffffff;
  --bg:#f1f1f4;
  --line:#d9d9e3;
  --ghost:rgba(43,39,115,.07);
  --grey:#6d6d7c;
}
*{box-sizing:border-box;margin:0;padding:0}
html,body{width:1200px;height:264px;overflow:hidden}
body{background:linear-gradient(180deg,#fafafc,var(--bg));font-family:"Lato",sans-serif;position:relative}
.piece{position:absolute;background:var(--paper);box-shadow:0 1px 4px rgba(0,0,0,.18)}
.brand{display:flex;align-items:center;gap:4px;color:var(--navy);font-family:"Cinzel",serif;font-weight:600;white-space:nowrap}
.brand .mark{background:var(--navy);flex:none}
.brand.light{color:#fff}
.brand.light .mark{background:#fff}
.ghost{position:absolute;display:flex;flex-direction:column;align-items:center;gap:6px}
.ghost .sq{border:3px solid var(--ghost);background:var(--ghost)}
.ghost span{font-family:"Cinzel",serif;font-weight:600;color:var(--ghost);font-size:9px;white-space:nowrap}
.small{font-size:4px;color:var(--grey);line-height:1.4}
/* title card */
.title-card{left:12px;top:12px;width:132px;height:84px;padding:10px}
.title-card .brand{font-size:8px}
.title-card .brand .mark{width:14px;height:14px}
.title-card p{font-size:7px;color:var(--grey);margin-top:8px;font-style:italic}
.mini-card{left:10px;width:130px;height:38px;padding:6px}
.mini-card .brand{font-size:6px}
.mini-card .brand .mark{width:9px;height:9px}
/* letterheads */
.letterhead{top:12px;width:188px;height:240px;display:flex;flex-direction:column;align-items:center;padding-top:12px}
.letterhead .brand{font-size:6px;flex-direction:column;gap:2px}
.letterhead .brand .mark{width:14px;height:14px}
.letterhead .ghost{top:70px}
.letterhead .ghost .sq{width:70px;height:70px}
.letterhead footer{position:absolute;bottom:8px;left:12px;right:12px;border-top:1px solid var(--line);padding-top:3px;text-align:center}
/* business cards */
.bcard{left:552px;width:144px;height:40px;padding:6px;display:flex;align-items:center;justify-content:space-between}
.bcard .brand{font-size:6px}
.bcard .brand .mark{width:10px;height:10px}
.bcard.back{background:var(--navy);justify-content:center}
.bcard .band{position:absolute;left:0;right:0;bottom:0;height:6px;background:var(--navy)}
/* envelopes */
.envelope{left:708px;width:192px;height:64px;overflow:hidden}
.envelope .flap{position:absolute;inset:0}
.envelope .brand{position:absolute;left:8px;top:8px;font-size:5px}
.envelope .brand .mark{width:8px;height:8px}
/* folder */
.folder{top:66px;height:186px}
.folder.inside{left:912px;width:138px}
.folder.inside .pocket{position:absolute;left:0;right:0;bottom:0;height:70px;background:var(--navy)}
.folder.inside .slot{position:absolute;left:14px;top:6px;width:40px;height:22px;border:1px solid rgba(255,255,255,.5)}
.folder.cover{left:1050px;width:138px;background:var(--navy);padding:14px 10px}
.folder.cover .brand{font-size:6px}
.folder.cover .brand .mark{width:12px;height:12px}
.folder.cover .ghost{left:10px;top:20px}
.folder.cover .ghost .sq{width:90px;height:90px;border-color:rgba(255,255,255,.07);background:rgba(255,255,255,.06)}
.folder.cover .ghost span{color:rgba(255,255,255,.08)}
.folder.cover .tag{position:absolute;bottom:12px;left:10px;font-size:5px;color:#c9c8e6;letter-spacing:1px}
</style>
</head>
<body>

<section class="piece title-card">
  <div class="brand"><i class="mark"></i>Daniel R Halvorsen</div>
  <p>Stationery Concepts</p>
</section>

<section class="piece mini-card" style="top:168px">
  <div class="brand"><i class="mark"></i>Daniel R Halvorsen</div>
</section>
<section class="piece mini-card" style="top:212px;background:var(--navy)">
  <div class="brand light"><i class="mark"></i>Daniel R Halvorsen</div>
</section>

<section class="piece letterhead" style="left:150px">
  <div class="brand"><i class="mark"></i>Daniel R Halvorsen</div>
  <div class="ghost"><i class="sq"></i><span>Daniel R Halvorsen</span></div>
  <footer class="small">418 N. 7th Street · Columbus, OH 43207 · VerdictWithHalvorsen.example</footer>
</section>

<section class="piece letterhead" style="left:348px">
  <div class="brand"><i class="mark"></i>Daniel R Halvorsen</div>
  <div class="ghost"><i class="sq"></i><span>Daniel R Halvorsen</span></div>
  <footer class="small">Daniel@verdictwithhalvorsen.example · VerdictWithHalvorsen.example</footer>
</section>

<section class="piece bcard" style="top:84px">
  <div class="brand"><i class="mark"></i>Daniel R Halvorsen</div>
  <div class="small">Attorney at Law</div>
</section>
<section class="piece bcard back" style="top:130px">
  <div class="brand light"><i class="mark"></i>Daniel R Halvorsen</div>
</section>
<section class="piece bcard" style="top:176px">
  <div class="small">418 N. 7th Street<br>Columbus, OH 43207<br>Daniel@verdictwithhalvorsen.example</div>
  <span class="band"></span>
</section>

<section class="piece envelope" style="top:96px">
  <svg class="flap" viewBox="0 0 192 64" preserveAspectRatio="none"><polygon points="0,0 192,0 96,38" fill="var(--navy)"/></svg>
</section>
<section class="piece envelope" style="top:176px">
  <svg class="flap" viewBox="0 0 192 64" preserveAspectRatio="none"><rect x="0" y="54" width="192" height="10" fill="var(--navy)"/></svg>
  <div class="brand"><i class="mark"></i>Daniel R Halvorsen</div>
</section>

<section class="piece folder inside">
  <div class="pocket"><i class="slot"></i></div>
</section>
<section class="piece folder cover">
  <div class="ghost"><i class="sq"></i><span>Daniel R Halvorsen</span></div>
  <div class="brand light"><i class="mark"></i>Daniel R Halvorsen</div>
  <div class="tag">CRIMINAL DEFENSE</div>
</section>

</body>
</html>
```